Corporate consulting business needs a business card

I want a professional business card.... surprise me

Target Market(s)

Corprorate and Not for Profit firms and organisations

Industry/Entity Type

Consulting

Contact Information for Business Card

Logo
Corporate Consulting Services
On Time, On Budget, Beyond Expectation
Tobin Averley
Director
0427 31 64 92 (Larger)
tobin@ta-advisory.com.au
www.ta-advisory.com.au
include little icons beside the contact info:

- Envelope = email
- Phone = phone
- Globe = website

Font styles to use
Serif
Sans Serif

Requirements
Must have
• Professional and clean
Nice to have
• you tell me

```html
<!DOCTYPE html>
<html lang="en">
<head>
<meta charset="utf-8">
<title>TA Advisory Services – Business Card</title>
<link href="https://fonts.googleapis.com/css2?family=Cinzel:wght@400;700&family=Open+Sans:wght@400;600&display=swap" rel="stylesheet">
<style>
  :root {
    --backdrop: #e6e6e6;
    --card-white: #ffffff;
    --card-black: #050505;
    --ink: #1c1c1c;
    --brown: #5a3a22;
    --white: #ffffff;
    --grey-text: #bdbdbd;
  }
  * { margin: 0; padding: 0; box-sizing: border-box; }
  html, body {
    width: 1200px; height: 900px; overflow: hidden;
    background: var(--backdrop);
  }
  .canvas { position: relative; width: 1200px; height: 900px; }

  .card {
    position: absolute; width: 560px; height: 320px;
    box-shadow: 0 6px 14px rgba(0,0,0,0.18);
  }

  /* Back of card */
  .card-back {
    left: 70px; top: 110px; background: var(--card-black);
    display: flex; flex-direction: column; align-items: center; justify-content: center;
    color: var(--white);
  }
  .brand {
    display: flex; align-items: center; gap: 14px;
    font-family: "Cinzel", serif; font-weight: 700;
  }
  .brand-dot {
    border-radius: 50%; border: 3px solid currentColor; flex: none;
  }
  .card-back .brand { font-size: 26px; letter-spacing: 0.5px; }
  .card-back .brand-dot { width: 58px; height: 58px; }
  .back-url {
    margin-top: 30px;
    font-family: "Open Sans", sans-serif; font-size: 12px;
    letter-spacing: 2px; color: var(--grey-text);
  }

  /* Front of card */
  .card-front {
    left: 570px; top: 470px; background: var(--card-white);
    font-family: "Open Sans", sans-serif; color: var(--ink);
  }
  .card-front .brand {
    position: absolute; right: 34px; top: 34px;
    font-size: 15px; color: var(--brown); gap: 10px;
  }
  .card-front .brand-dot { width: 34px; height: 34px; border-width: 2px; }
  .tagline {
    position: absolute; left: 34px; top: 132px;
    font-size: 11.5px; letter-spacing: 1.6px;
  }
  .rule {
    position: absolute; left: 34px; right: 34px; top: 196px;
    height: 1px; background: var(--brown);
  }
  .person-name {
    position: absolute; left: 34px; top: 168px;
    font-family: "Cinzel", serif; font-weight: 700; font-size: 19px;
    color: var(--brown); letter-spacing: 0.5px;
  }
  .person-role {
    position: absolute; left: 34px; top: 206px;
    font-size: 11.5px; letter-spacing: 1.2px;
  }
  .contact-list {
    position: absolute; left: 34px; top: 236px; list-style: none;
  }
  .contact-list li {
    display: flex; align-items: center; gap: 12px;
    font-size: 12px; letter-spacing: 1.4px; margin-bottom: 8px;
  }
  .contact-list .phone-number { font-size: 13.5px; }
  .contact-icon { width: 14px; height: 14px; flex: none; }
  .address {
    position: absolute; right: 34px; top: 210px; text-align: right;
    font-size: 11.5px; letter-spacing: 1.3px; line-height: 1.55;
  }
  .address .web {
    margin-top: 6px; font-weight: 600; color: var(--brown);
  }
</style>
</head>
<body>
<main class="canvas">
  <section class="card card-back" aria-label="Card back">
    <div class="brand"><span class="brand-dot"></span><span>TA Advisory Services</span></div>
    <p class="back-url">www.ta-advisory.com.au</p>
  </section>

  <section class="card card-front" aria-label="Card front">
    <div class="brand"><span class="brand-dot"></span><span>TA Advisory Services</span></div>
    <p class="tagline">On Time, On Budget, Beyond Expectation</p>
    <h1 class="person-name">Tobin Averley</h1>
    <div class="rule"></div>
    <p class="person-role">Director</p>
    <ul class="contact-list">
      <li>
        <svg class="contact-icon" viewBox="0 0 14 14" aria-hidden="true">
          <rect x="3.5" y="1" width="7" height="12" rx="1.2" fill="none" stroke="#5a3a22" stroke-width="1.6"/>
        </svg>
        <span class="phone-number">0427 31 64 92</span>
      </li>
      <li>
        <svg class="contact-icon" viewBox="0 0 14 14" aria-hidden="true">
          <rect x="1" y="3" width="12" height="9" fill="none" stroke="#5a3a22" stroke-width="1.6"/>
          <path d="M1 3 L7 8 L13 3" fill="none" stroke="#5a3a22" stroke-width="1.4"/>
        </svg>
        <span>tobin@ta-advisory.com.au</span>
      </li>
    </ul>
    <div class="address">
      <p>Harwood Lane Complex</p>
      <p>Bayview, Australia 2104</p>
      <p class="web">www.ta-advisory.com.au</p>
    </div>
  </section>
</main>
</body>
</html>
```